IT Services company general flyer

Looking for a printable US letter size flyer to give a brief overview of the services we offer. We also partner with another company for their services as well. Please check out our website at www.gearbymarlon.com and click on "Our Services" to learn about our services and visit www.bluepinesafety,com and click on services to learn about their services. Several of our services do overlap, so they only need to be on the flyer once. Let me know if this is too much content and we need to weed some out. We do not want Home phone service on this flyer. The basic design of the flyer should mimic similar to the VOIP one you did for me for the colors and logo. Also check out the "Who Choose us" page on www.gearbymarlon.com to include some of that as well.
Updates

Gathering more feedback

Target Market(s)

Targeting Small businesses that may not normally have a budget for their IT Services

Industry/Entity Type

It Service

Font styles to use
Serif
Sans Serif

Requirements
Must have
• Must include my logo, phone number and email/website address and must follow the same basic template of my previous flyers.

```html
<!DOCTYPE html>
<html lang="en">
<head>
<meta charset="utf-8">
<title>Gear By Marlon – IT Flyers</title>
<link href="https://fonts.googleapis.com/css2?family=Fira+Sans:wght@400;500;600;700;800&family=Open+Sans:wght@400;600;700&display=swap" rel="stylesheet">
<style>
  :root{
    --navy:#13245a;
    --navy-deep:#0c1a44;
    --red:#a3201f;
    --red-deep:#8a1d1d;
    --ink:#1b1f2e;
    --paper:#ffffff;
    --paper-soft:#f1f2f5;
    --stage:#6d6d6d;
    --sky:#2a8fb8;
  }
  *{box-sizing:border-box;margin:0;padding:0}
  html,body{width:1200px;height:818px;overflow:hidden}
  body{background:var(--stage);font-family:"Open Sans",Arial,sans-serif;color:var(--ink);position:relative}
  .flyer{position:absolute;width:525px;height:680px;background:var(--paper);overflow:hidden;box-shadow:0 6px 18px rgba(0,0,0,.35)}
  .flyer--intro{left:59px;top:70px}
  .flyer--services{left:620px;top:70px;width:522px}
  .abs{position:absolute}

  /* brand */
  .brand{display:flex;align-items:center;gap:10px}
  .brand__mark{width:40px;height:40px;background:var(--navy)}
  .brand__name{font-family:"Fira Sans",Arial,sans-serif;font-weight:600;color:var(--navy);font-size:21px;line-height:22px;border-left:1px solid #c9ccd6;padding-left:10px}

  /* intro flyer */
  .hero-art{left:0;top:0;width:525px;height:238px}
  .title{left:36px;top:100px;font-family:"Fira Sans",Arial,sans-serif;font-weight:800;font-size:31px;line-height:32px;color:var(--navy)}
  .title span{color:var(--red)}
  .band{left:0;top:238px;width:525px;height:127px;background:linear-gradient(90deg,#1b2f6e,#0d1b48)}
  .portrait{left:42px;top:168px;width:144px;height:197px;background:linear-gradient(180deg,#c9b8a6,#1c2a52 55%,#14204a);border-radius:60px 60px 0 0}
  .band__text{left:220px;top:254px;width:282px;color:#fff;font-size:11.2px;line-height:15.3px}
  .why{left:38px;top:384px;font-family:"Fira Sans",Arial,sans-serif;font-weight:700;font-size:27px;color:var(--navy)}
  .why span{color:var(--red)}
  .point{width:225px}
  .point--narrow{width:200px}
  .point__head{display:flex;align-items:center;gap:6px;font-family:"Fira Sans",Arial,sans-serif;font-weight:500;font-size:12.6px;color:var(--red);margin-left:-18px}
  .point__head svg{flex:none}
  .point__body{margin-top:6px;border-left:1px solid var(--navy);padding-left:12px;margin-left:-12px;font-size:7.5px;line-height:10.5px;text-align:justify;color:#222}
  .cta{left:297px;top:542px;font-family:"Fira Sans",Arial,sans-serif;font-size:17px;line-height:21.5px;color:var(--navy)}
  .cta b{color:var(--red);font-weight:600}

  .foot-red{left:0;top:630px;width:190px;height:50px;background:linear-gradient(90deg,#b0221f,#8a1d1d);color:#fff;padding:5px 0 0 16px}
  .foot-phone{display:flex;align-items:center;gap:5px;font-family:"Fira Sans",Arial,sans-serif;font-weight:700;font-size:20px;line-height:22px}
  .foot-mail{display:flex;align-items:center;gap:7px;font-size:10.5px;margin-top:2px}
  .foot-navy{left:180px;top:646px;width:345px;height:34px;background:var(--navy)}
  .foot-web{left:215px;top:652px;color:#fff;font-family:"Fira Sans",Arial,sans-serif;font-weight:500;font-size:14px;letter-spacing:.3px}
  .foot-social{left:409px;top:630px;width:116px;height:50px;background:var(--navy-deep);color:#fff;text-align:center;font-size:6px;padding-top:5px}
  .foot-social i{display:block;width:15px;height:15px;background:#fff;margin:4px auto 3px;border-radius:2px}
  .foot-social small{font-size:5px;display:block}

  /* services flyer */
  .tech-art{left:0;top:24px;width:522px;height:222px}
  .logo-tab{left:0;top:0;width:522px;height:92px}
  .brand--svc{left:330px;top:26px}
  .services-band{left:0;top:246px;width:522px;height:79px;background:linear-gradient(90deg,#8b1e1e,#a0302a 50%,#8b1e1e)}
  .services-title{left:135px;top:246px;width:254px;height:32px}
  .services-title h2{position:absolute;inset:0;text-align:center;color:#fff;font-family:"Fira Sans",Arial,sans-serif;font-weight:800;font-size:22px;line-height:32px;letter-spacing:.5px}
  .services-lead{left:30px;top:284px;width:462px;text-align:center;color:#fff;font-size:11.8px;line-height:16.5px}
  .grid-bg{left:0;top:325px;width:522px;height:300px;background:linear-gradient(180deg,#fff,#f0f1f4)}
  .service{display:flex;align-items:center;position:absolute;height:40px}
  .service svg{width:40px;height:40px;flex:none;fill:none;stroke:var(--red);stroke-width:2;stroke-linecap:round;stroke-linejoin:round}
  .service__rule{width:1px;height:36px;background:var(--red);margin:0 10px 0 17px}
  .service__name{font-family:"Fira Sans",Arial,sans-serif;font-weight:600;font-size:11px;line-height:14px;color:var(--navy-deep)}

  .svc-foot-tab{left:0;top:628px;width:128px;height:16px;background:var(--navy);color:#fff;font-size:7.5px;padding:3px 0 0 14px;clip-path:polygon(0 0,92% 0,100% 100%,0 100%)}
  .svc-foot-tab i{display:inline-block;width:8px;height:8px;background:#fff;margin-left:6px;vertical-align:-1px;border-radius:1px}
  .svc-foot-red{left:0;top:643px;width:340px;height:32px;background:linear-gradient(90deg,#8b1e1e,#a6231f);clip-path:polygon(0 0,100% 0,94% 100%,0 100%)}
  .svc-foot-web{left:14px;top:648px;color:#fff;font-size:14px;letter-spacing:1.6px}
  .svc-contact{left:236px;top:627px;width:100px;height:16px;background:#e7e8ec;font-size:11.5px;color:var(--ink);text-align:center;line-height:16px;clip-path:polygon(6% 0,100% 0,100% 100%,0 100%)}
  .svc-foot-navy{left:318px;top:620px;width:204px;height:55px;background:var(--navy);clip-path:polygon(10% 0,100% 0,100% 100%,0 100%);color:#fff;padding:4px 0 0 32px}
  .svc-foot-navy .foot-phone{font-size:18.5px}
</style>
</head>
<body>

<!-- Intro flyer -->
<section class="flyer flyer--intro">
  <svg class="abs hero-art" viewBox="0 0 525 238" role="img" aria-label="Photo of an open hand holding a glowing network globe of connected tech icons">
    <defs>
      <radialGradient id="globeGlow" cx="70%" cy="40%" r="65%">
        <stop offset="0" stop-color="#3a6fd8"/>
        <stop offset=".5" stop-color="#1a2f8a"/>
        <stop offset="1" stop-color="#0a1240"/>
      </radialGradient>
    </defs>
    <polygon points="240,0 525,0 525,238 240,238 306,118" fill="url(#globeGlow)"/>
  </svg>

  <div class="abs brand" style="left:39px;top:30px">
    <span class="brand__mark"></span>
    <span class="brand__name">GEAR<br>BY MARLON</span>
  </div>

  <h1 class="abs title">IT CONSULTING<br><span>&amp; SERVICES</span></h1>

  <div class="abs band"></div>
  <div class="abs portrait" role="img" aria-label="Photo of a smiling consultant in a suit giving a thumbs up while holding a laptop"></div>
  <p class="abs band__text">At Gear By Marlon, we provide complete managed IT services tailored for your small and medium business. We understand small business because we are small business. We can help bring enterprise technology solutions to your business.</p>

  <h2 class="abs why"><span>Why Choose</span> Gear By Marlon?</h2>

  <article class="abs point" style="left:56px;top:438px">
    <h3 class="point__head"><svg width="12" height="12" viewBox="0 0 12 12"><circle cx="6" cy="6" r="5" fill="none" stroke="#13245a"/><path d="M3.5 6.2l1.8 1.7 3.2-3.4" fill="none" stroke="#13245a"/></svg>Personalized Solutions and Support</h3>
    <p class="point__body">We know your time is valuable and your technology is critical. That's why we take time to visit with each of our clients and recommend the best solutions for them. You're not just another client to us, you are a partner. We want to help you be successful.</p>
  </article>

  <article class="abs point point--narrow" style="left:303px;top:438px">
    <h3 class="point__head"><svg width="12" height="12" viewBox="0 0 12 12"><circle cx="6" cy="6" r="5" fill="none" stroke="#13245a"/><path d="M3.5 6.2l1.8 1.7 3.2-3.4" fill="none" stroke="#13245a"/></svg>One Stop Shop</h3>
    <p class="point__body" style="text-align:left">We can help you with all your IT needs, weather it be computer or network security, phone and voice needs, or cloud services. Contact us today to discuss how we can help you.</p>
  </article>

  <article class="abs point" style="left:56px;top:529px">
    <h3 class="point__head"><svg width="12" height="12" viewBox="0 0 12 12"><circle cx="6" cy="6" r="5" fill="none" stroke="#13245a"/><path d="M3.5 6.2l1.8 1.7 3.2-3.4" fill="none" stroke="#13245a"/></svg>Experience</h3>
    <p class="point__body">We have years of experience in both large and small environments. We know what solutions are available and how to implement them in your business. We are constantly working with industry experts and the ever changing technology landscape.</p>
  </article>

  <p class="abs cta">Get peace of mind<br>and <b>Schedule a<br>Technology Assessment</b></p>

  <div class="abs foot-navy"></div>
  <div class="abs foot-red">
    <div class="foot-phone"><svg width="16" height="16" viewBox="0 0 16 16"><circle cx="8" cy="8" r="7" fill="none" stroke="#fff" stroke-width="1.3"/><path d="M5.3 4.5l1.4-.3.8 1.8-.9.7c.4 1 1.2 1.8 2.2 2.2l.7-.9 1.8.8-.3 1.4c-3 .2-5.9-2.7-5.7-5.7z" fill="#fff"/></svg>555.014.0288</div>
    <div class="foot-mail"><svg width="12" height="9" viewBox="0 0 12 9"><rect width="12" height="9" rx="1" fill="#fff"/><path d="M.5 .8L6 5l5.5-4.2" fill="none" stroke="#a3201f"/></svg>sales@gearbymarlon.com</div>
  </div>
  <div class="abs foot-web">www.gearbymarlon.com</div>
  <div class="abs foot-social">FOLLOW US ON<i></i><small>social/gearbymarlon</small></div>
</section>

<!-- Services flyer -->
<section class="flyer flyer--services">
  <svg class="abs tech-art" viewBox="0 0 522 222" role="img" aria-label="Photo of a hand touching a cloud icon on a blue digital interface with hexagon icons">
    <defs>
      <linearGradient id="skyTech" x1="0" y1="0" x2="1" y2="1">
        <stop offset="0" stop-color="#1d6f99"/>
        <stop offset=".5" stop-color="#2a9cc4"/>
        <stop offset="1" stop-color="#186283"/>
      </linearGradient>
    </defs>
    <rect width="522" height="222" fill="url(#skyTech)"/>
  </svg>
  <svg class="abs logo-tab" viewBox="0 0 522 92" aria-hidden="true">
    <polygon points="0,0 522,0 522,91 331,91 282,24 0,24" fill="#fff"/>
    <line x1="282" y1="24" x2="331" y2="91" stroke="#13245a" stroke-width="1.2"/>
    <line x1="331" y1="91" x2="522" y2="91" stroke="#13245a" stroke-width="1.2"/>
  </svg>
  <div class="abs brand brand--svc">
    <span class="brand__mark"></span>
    <span class="brand__name">GEAR<br>BY MARLON</span>
  </div>

  <div class="abs services-band"></div>
  <div class="abs services-title">
    <svg width="254" height="32" viewBox="0 0 254 32" aria-hidden="true"><polygon points="0,0 254,0 240,32 14,32" fill="#13245a"/></svg>
    <h2>OUR SERVICES</h2>
  </div>
  <p class="abs services-lead">We provide a complete range of IT services focused on you getting the most from your technology.</p>

  <div class="abs grid-bg"></div>

  <!-- row 1 -->
  <div class="service" style="left:44px;top:356px">
    <svg viewBox="0 0 40 40"><circle cx="20" cy="12" r="5"/><circle cx="20" cy="12" r="9" stroke-dasharray="3 3"/><path d="M4 18v10l6 6M36 18v10l-6 6M10 34h-4v5h8v-5M30 34h4v5h-8v-5M9 26l5 3M31 26l-5 3"/></svg>
    <span class="service__rule"></span><span class="service__name">Managed<br>IT Services</span>
  </div>
  <div class="service" style="left:201px;top:356px">
    <svg viewBox="0 0 40 40"><ellipse cx="24" cy="16" rx="13" ry="9"/><path d="M8 14c-3 4-1 14 8 20l4-4-4-4-3 2c-2-3-2-7-1-10"/><path d="M33 4c2 1 4 3 4 5"/></svg>
    <span class="service__rule"></span><span class="service__name">Business VOIP<br>Phone Service</span>
  </div>
  <div class="service" style="left:371px;top:356px">
    <svg viewBox="0 0 40 40"><path d="M20 2l15 5v12c0 10-7 16-15 19C12 35 5 29 5 19V7z"/><path d="M20 7l10 3v9c0 7-5 11-10 13-5-2-10-6-10-13v-9z"/><rect x="13" y="15" width="14" height="10"/><path d="M13 15l7 6 7-6"/></svg>
    <span class="service__rule"></span><span class="service__name">Email<br>Security</span>
  </div>

  <!-- row 2 -->
  <div class="service" style="left:44px;top:419px">
    <svg viewBox="0 0 40 40"><rect x="2" y="3" width="30" height="9" rx="3"/><rect x="2" y="14" width="30" height="9" rx="3"/><rect x="2" y="25" width="22" height="9" rx="3"/><circle cx="7" cy="7.5" r="1.5"/><circle cx="13" cy="7.5" r="1.5"/><circle cx="7" cy="18.5" r="1.5"/><circle cx="13" cy="18.5" r="1.5"/><rect x="27" y="29" width="11" height="9"/><path d="M29 29v-3a3.5 3.5 0 0 1 7 0v3"/></svg>
    <span class="service__rule"></span><span class="service__name">Network<br>Security</span>
  </div>
  <div class="service" style="left:201px;top:419px">
    <svg viewBox="0 0 40 40"><rect x="3" y="26" width="34" height="9" rx="3"/><path d="M8 30.5h2M13 30.5h2M18 30.5h2M28 26V12"/><path d="M23 11a7 7 0 0 1 10 0M20 7a11 11 0 0 1 16 0"/></svg>
    <span class="service__rule"></span><span class="service__name">Wireless<br>Solutions</span>
  </div>
  <div class="service" style="left:371px;top:419px">
    <svg viewBox="0 0 40 40"><rect x="3" y="4" width="34" height="24" rx="2"/><path d="M14 34h12M20 28v6M20 7l8 3v6c0 5-4 8-8 9-4-1-8-4-8-9v-6z"/></svg>
    <span class="service__rule"></span><span class="service__name">Web<br>Security</span>
  </div>

  <!-- row 3 -->
  <div class="service" style="left:44px;top:484px">
    <svg viewBox="0 0 40 40"><rect x="4" y="4" width="32" height="32" rx="2"/><path d="M10 13h20M10 20h20M10 27h20"/></svg>
    <span class="service__rule"></span><span class="service__name">Productivity<br>Suite</span>
  </div>
  <div class="service" style="left:201px;top:484px">
    <svg viewBox="0 0 40 40"><circle cx="20" cy="20" r="11"/><circle cx="20" cy="20" r="7"/><rect x="17" y="19" width="6" height="5"/><path d="M18 19v-2a2 2 0 0 1 4 0v2M20 2v7M20 31v7M2 20h7M31 20h7M7 7l5 5M28 28l5 5M33 7l-5 5M12 28l-5 5"/></svg>
    <span class="service__rule"></span><span class="service__name">Endpoint<br>Security</span>
  </div>
  <div class="service" style="left:371px;top:484px">
    <svg viewBox="0 0 40 40"><path d="M9 20a6 6 0 0 1 1-11 9 9 0 0 1 17-1 6 6 0 0 1 4 12z"/><path d="M20 20v6M8 26h24M8 26v4M20 26v4M32 26v4"/><rect x="4" y="30" width="8" height="6"/><rect x="16" y="30" width="8" height="6"/><rect x="28" y="30" width="8" height="6"/></svg>
    <span class="service__rule"></span><span class="service__name">Cloud<br>Services</span>
  </div>

  <!-- row 4 -->
  <div class="service" style="left:44px;top:558px">
    <svg viewBox="0 0 40 40"><rect x="5" y="8" width="30" height="22" rx="2"/><path d="M2 30h36v3H2zM20 11l7 2.5v5c0 4-3 6-7 7.5-4-1.5-7-3.5-7-7.5v-5z"/><path d="M17 18l2 2 4-4"/></svg>
    <span class="service__rule"></span><span class="service__name">Cybersecurity<br>Assessments</span>
  </div>
  <div class="service" style="left:201px;top:558px">
    <svg viewBox="0 0 40 40"><rect x="4" y="6" width="32" height="24" rx="2"/><path d="M14 35h12M20 30v5"/><circle cx="20" cy="16" r="6"/><circle cx="17.5" cy="15.5" r="1.2"/><circle cx="22.5" cy="15.5" r="1.2"/><path d="M13 24l14-2M13 22l14 2"/></svg>
    <span class="service__rule"></span><span class="service__name">Ransomware &amp;<br>Threat Response</span>
  </div>
  <div class="service" style="left:371px;top:558px">
    <svg viewBox="0 0 40 40"><rect x="3" y="3" width="34" height="8" rx="1"/><rect x="3" y="29" width="34" height="8" rx="1"/><path d="M7 7h10M7 33h10M28 7h1M32 7h1M28 33h1M32 33h1M13 14v10M10 21l3 3 3-3M27 26V16M24 19l3-3 3 3"/></svg>
    <span class="service__rule"></span><span class="service__name">Backup &amp;<br>Disaster<br>Recovery</span>
  </div>

  <!-- footer -->
  <div class="abs svc-foot-tab">VISIT US AT<i></i></div>
  <div class="abs svc-foot-red"></div>
  <div class="abs svc-foot-web">www.gearbymarlon.com</div>
  <div class="abs svc-contact">CONTACT US</div>
  <div class="abs svc-foot-navy">
    <div class="foot-phone"><svg width="15" height="15" viewBox="0 0 16 16"><circle cx="8" cy="8" r="7" fill="none" stroke="#fff" stroke-width="1.3"/><path d="M5.3 4.5l1.4-.3.8 1.8-.9.7c.4 1 1.2 1.8 2.2 2.2l.7-.9 1.8.8-.3 1.4c-3 .2-5.9-2.7-5.7-5.7z" fill="#fff"/></svg>555.014.0288</div>
    <div class="foot-mail"><svg width="12" height="9" viewBox="0 0 12 9"><rect width="12" height="9" rx="1" fill="#fff"/><path d="M.5 .8L6 5l5.5-4.2" fill="none" stroke="#13245a"/></svg>sales@gearbymarlon.com</div>
  </div>
</section>

</body>
</html>
```